Company raising consciousness thru leadership & self-awareness needs amazing Letterhead

We are a technology company that spun out of a consulting firm. We are waking people up in corporate America through surveys, leadership development, workshops and consulting. Getting employees to become self-aware and changing company culture through improved leadership and team effectiveness. We need Word letterhead for our proposals, handouts, and worksheets that match our brand standard, is fresh, and communicates trust, credibility and professionalism.

Target Market(s)

Our target clients are other businesses, and executive leaders and C-suite leaders in those companies.

Font styles to use
Sans Serif

Requirements
Must have
• A Word template we can use for handouts, proposals, executive summary, project management documents, and letters. We need our logo. Please add page number and date on the footer. Must match the theme of our new website in look and feel to match the brand we are trying to promote. Use the colors from our brand standard document I submitted.

```html
<!DOCTYPE html>
<html lang="en">
<head>
<meta charset="utf-8">
<title>Veralume Leadership Letterhead</title>
<link href="https://fonts.googleapis.com/css2?family=Lato:wght@400;700&display=swap" rel="stylesheet">
<style>
  :root {
    --navy: #1f3c78;
    --purple: #7d3fa6;
    --paper: #fffffd;
    --backdrop: #cfc5c2;
    --rule: #5a6f9e;
  }
  * { margin: 0; padding: 0; box-sizing: border-box; }
  html, body {
    width: 1200px;
    height: 784px;
    overflow: hidden;
    background: var(--backdrop);
    font-family: "Lato", sans-serif;
  }
  .letterhead {
    position: absolute;
    left: 314px;
    top: 22px;
    width: 572px;
    height: 740px;
    background: var(--paper);
    box-shadow: 0 4px 14px rgba(60, 40, 40, 0.18);
    overflow: hidden;
  }
  .brand {
    position: absolute;
    left: 36px;
    top: 38px;
    display: flex;
    align-items: center;
    gap: 9px;
  }
  .brand-dot {
    width: 22px;
    height: 22px;
    border-radius: 50%;
    background: var(--navy);
  }
  .brand-name {
    font-weight: 700;
    font-size: 17px;
    color: var(--navy);
    letter-spacing: 0.2px;
  }
  .contact {
    position: absolute;
    right: 34px;
    top: 30px;
    display: flex;
    gap: 12px;
  }
  .contact-divider {
    width: 1.5px;
    background: var(--purple);
  }
  .contact-list {
    list-style: none;
    font-size: 10.5px;
    line-height: 15px;
    color: var(--navy);
  }
  .contact-list li {
    display: flex;
    align-items: center;
    gap: 5px;
  }
  .contact-list .no-icon { padding-left: 15px; }
  .contact-list svg {
    width: 10px;
    height: 10px;
    flex: none;
  }
  .footer-field {
    position: absolute;
    bottom: 34px;
    display: flex;
    align-items: flex-end;
    gap: 4px;
    font-size: 12px;
    color: var(--navy);
  }
  .footer-field .fill-line {
    width: 78px;
    border-bottom: 1px solid var(--rule);
    margin-bottom: 2px;
  }
  .date-field { left: 36px; }
  .page-field { right: 30px; }
  .footer-band {
    position: absolute;
    left: 0;
    bottom: 0;
    width: 100%;
    height: 12px;
    display: flex;
    gap: 3px;
  }
  .footer-band .accent {
    width: 26px;
    background: var(--purple);
  }
  .footer-band .bar {
    flex: 1;
    background: var(--navy);
  }
</style>
</head>
<body>
  <main class="letterhead">
    <header>
      <div class="brand">
        <span class="brand-dot"></span>
        <span class="brand-name">Veralume Leadership</span>
      </div>

      <div class="contact">
        <span class="contact-divider"></span>
        <ul class="contact-list">
          <li class="no-icon">1234 First Line Address</li>
          <li class="no-icon">5678 Second Line Address</li>
          <li>
            <svg viewBox="0 0 10 10" aria-hidden="true"><path d="M2 1 L4 1 L4.6 3 L3.6 3.8 Q4.6 5.6 6.2 6.4 L7 5.4 L9 6 L9 8 Q5 9 2.6 6.6 Q1 4.6 2 1 Z" fill="var(--purple)"/></svg>
            (111) 999-0000
          </li>
          <li>
            <svg viewBox="0 0 10 10" aria-hidden="true"><rect x="0.5" y="2" width="9" height="6.5" fill="var(--purple)"/><path d="M0.8 2.4 L5 5.6 L9.2 2.4" stroke="#fff" stroke-width="0.9" fill="none"/></svg>
            info@yourmail.com
          </li>
          <li>
            <svg viewBox="0 0 10 10" aria-hidden="true"><circle cx="5" cy="5" r="4.2" fill="none" stroke="var(--purple)" stroke-width="1"/><ellipse cx="5" cy="5" rx="1.8" ry="4.2" fill="none" stroke="var(--purple)" stroke-width="0.8"/><path d="M1 5 H9" stroke="var(--purple)" stroke-width="0.8"/></svg>
            www.yourwesite.com
          </li>
        </ul>
      </div>
    </header>

    <footer>
      <div class="footer-field date-field">
        <span>Date:</span><span class="fill-line"></span>
      </div>
      <div class="footer-field page-field">
        <span>Page:</span><span class="fill-line"></span>
      </div>
      <div class="footer-band">
        <span class="accent"></span>
        <span class="bar"></span>
      </div>
    </footer>
  </main>
</body>
</html>
```